I'm an electrician and the name of my company is called Brisk 'N' Bright Electrical. I require a professional business card that speaks to my clients, I also need it to be innovative and modern. We do maintenance & service work for domestic and commercial premises.

Industry/Entity Type

Electrical

Contact Information for Business Card

Must have the name of my company Brisk 'N' Bright Electrical, my name Darren Kolovich and my contact details 0427 318 592 and company email address Brisknbrightelectrical@quillpost.example and/or website Brisknbrightelectrical.example.au

Logo Text

Brisk 'N' Bright Electrical (If possible)

Colors
33a6d7
0592cd
3176b5

```html
<!DOCTYPE html>
<html lang="en">
<head>
<meta charset="utf-8">
<title>Brisk 'N' Bright Electrical – Business Card</title>
<link rel="stylesheet" href="https://fonts.googleapis.com/css2?family=Montserrat:wght@700;800&family=Arimo:wght@400&display=swap">
<style>
  :root {
    --backdrop: #d6d7d9;
    --card-light: #f4f4f5;
    --card-dark: #262626;
    --ink: #1b1b1b;
    --ink-soft: #2c2c2c;
    --accent: #33a6d7;
    --accent-deep: #0592cd;
    --logo-on-dark: #9a9a9a;
  }
  * { margin: 0; padding: 0; box-sizing: border-box; }
  html, body {
    width: 1200px;
    height: 900px;
    overflow: hidden;
    background: var(--backdrop);
  }
  .canvas {
    position: relative;
    width: 1200px;
    height: 900px;
  }
  .card {
    position: absolute;
    left: 320px;
    width: 560px;
    height: 320px;
    box-shadow: 0 10px 28px rgba(0,0,0,0.18);
  }
  .card-front { top: 90px; background: var(--card-light); }
  .card-back  { top: 490px; background: var(--card-dark); }

  .brand {
    position: absolute;
    display: flex;
    align-items: center;
    gap: 10px;
    font-family: 'Montserrat', sans-serif;
    font-weight: 800;
    text-transform: uppercase;
    line-height: 1.15;
  }
  .brand-front {
    top: 44px;
    right: 50px;
    color: var(--ink);
    font-size: 17px;
    letter-spacing: 0.5px;
    text-align: left;
  }
  .brand-dot {
    width: 14px;
    height: 14px;
    border-radius: 50%;
    background: var(--accent);
    flex: none;
  }
  .brand-back {
    inset: 0;
    justify-content: center;
    color: var(--logo-on-dark);
    font-size: 30px;
    letter-spacing: 1px;
    text-align: center;
  }

  .holder-name {
    position: absolute;
    left: 50px;
    top: 150px;
    font-family: 'Montserrat', sans-serif;
    font-weight: 700;
    font-size: 20px;
    color: var(--ink);
  }
  .rule {
    position: absolute;
    left: 50px;
    right: 48px;
    top: 182px;
    height: 2px;
    background: var(--accent-deep);
  }
  .contact-list {
    position: absolute;
    right: 32px;
    top: 192px;
    list-style: none;
    font-family: 'Arimo', sans-serif;
    font-size: 13.5px;
    color: var(--ink-soft);
  }
  .contact-item {
    display: flex;
    justify-content: flex-end;
    align-items: center;
    gap: 8px;
    height: 21px;
  }
  .contact-icon { width: 13px; height: 13px; flex: none; }
</style>
</head>
<body>
<main class="canvas">

  <section class="card card-front" aria-label="Business card front">
    <div class="brand brand-front">
      <span class="brand-dot"></span>
      <span>Brisk 'N' Bright<br>Electrical</span>
    </div>

    <h1 class="holder-name">Darren Kolovich</h1>
    <div class="rule"></div>

    <ul class="contact-list">
      <li class="contact-item">
        <span>0427 318 592</span>
        <svg class="contact-icon" viewBox="0 0 16 16" aria-hidden="true">
          <circle cx="8" cy="8" r="7" fill="none" stroke="#33a6d7" stroke-width="1.6"/>
          <path d="M5.3 4.6l1.4-.3.8 1.8-.9.7c.4.9 1.1 1.6 2 2l.7-.9 1.8.8-.3 1.4c-2.7.3-5.8-2.8-5.5-5.5z" fill="#33a6d7"/>
        </svg>
      </li>
      <li class="contact-item">
        <span>Brisknbrightelectrical@quillpost.example</span>
        <svg class="contact-icon" viewBox="0 0 16 16" aria-hidden="true">
          <rect x="1" y="3" width="14" height="10" rx="1" fill="#33a6d7"/>
          <path d="M1.5 3.8L8 9l6.5-5.2" fill="none" stroke="#f4f4f5" stroke-width="1.3"/>
        </svg>
      </li>
      <li class="contact-item">
        <span>Brisknbrightelectrical.example.au</span>
        <svg class="contact-icon" viewBox="0 0 16 16" aria-hidden="true">
          <circle cx="8" cy="8" r="7" fill="#33a6d7"/>
          <ellipse cx="8" cy="8" rx="3" ry="7" fill="none" stroke="#f4f4f5" stroke-width="1"/>
          <path d="M1 8h14M2.5 4.5h11M2.5 11.5h11" stroke="#f4f4f5" stroke-width="1"/>
        </svg>
      </li>
    </ul>
  </section>

  <section class="card card-back" aria-label="Business card back">
    <div class="brand brand-back">
      <span>Brisk 'N' Bright<br>Electrical</span>
    </div>
  </section>

</main>
</body>
</html>
```